Brochure Design Project

I am looking for a trifold brochure.
I would like it to be square (5.5 x 5.5)
The back needs to be reserved for a map and logo information.

we are a financial planning firm. we have been in operation for 15 years.
our clients are ecstatic and continue to refer others to us.

Brochure COPY:
Building Wealth, Building Futures
We start with your goals. Then we build a comprehensive strategy to manage your investments, grow your wealth, minimize your tax burden and protect your family. Most importantly, we keep you informed about market change, opportunities and concerns before they impact you, so you can make confident decisions about your future, every step of the way.

Understanding and Expertise (bios)
Steadfast Money Partners is led by Lorna Feldskov and Miriam Oakhurst, experienced business partners who take the time to listen to you, understand your needs and present you with all your options.
Our focus in on your future, and building a confident and financially secure path for you and your family for the years ahead.

Lorna Feldskov, BSc, MBA, CPA, CA, CFP, FMA, CPCA
Certified Financial Planner

With years of experience in tax, investment, estate and retirement issues - and an extensive business background - Lorna provided her clients with important financial insights and clear direction in a friendly and open manner.

Miriam Oakhurst, BSEd, FMA, CPCA, CFP, FCSI, CIM

After a successful tennis career Miriam joined Lorna in the financial industry. Miriam quickly discovered how much she enjoys working with people and helping them to achieve their goals. Leveraging the discipline and work ethic developed during her tennis career, Miriam has been instrumental in creating the successful process used by Steadfast Money Partners.

People Trust Us to Help Them
The important things in life are often neglected due to the demands of day to day, including financial planning and wealth management. But it doesn't have to be that way when you have a trustworthy team looking out for you.
At Steadfast Money Partners we have the knowledge, experience and resources to help you move forward and realize your financial goals.

(side note) on the back of the brochure it should have the SMP logo, the office address, 382 Kettlewood Rd. E. Mississauga, ON L5R 7M4, and our website address.

Reason: Am juggling a number of different projects so need to extend the deadline on this one. Will provide copy for the project by end of day today.

Target Market(s)

We would like the brochure to appeal to the high net worth client who is currently working with an advisor but is not getting the attention from them.

Industry/Entity Type

Financial

Requirements
Must have
• SMP Logo on the front. The logo is blue with black font and has a tagline with it that says "Choose your path, change your future."
you can see the logo at www.plantharvestsoon.ca

One page must be about the two advisors, Lorna Feldskov and Miriam Oakhurst.
(leave an open area for bios and we will fill it in)

We want it to talk about building wealth and passing it on to the next generation.
Should not have
• Financial lingo.

```html
<!DOCTYPE html>
<html lang="en">
<head>
<meta charset="utf-8">
<title>Steadfast Money Partners – Trifold Brochure Spread</title>
<link rel="stylesheet" href="https://fonts.googleapis.com/css2?family=Roboto:wght@300;400&family=PT+Sans:wght@400;700&display=swap">
<style>
  :root {
    --blue: #1f5c97;
    --navy: #2e3d68;
    --strip: #3b568a;
    --band: #6a80b0;
    --band-soft: rgba(120, 140, 190, 0.55);
    --white: #ffffff;
    --label: #666666;
    --text-light: #e8ecf5;
    --logo-ink: #2b2b2b;
  }
  * { box-sizing: border-box; margin: 0; padding: 0; }
  html, body { width: 1200px; height: 901px; overflow: hidden; background: var(--white); }
  body { position: relative; font-family: "PT Sans", sans-serif; }

  .sheet-frame { position: absolute; inset: 0; border: 1px solid #8a8a8a; }

  .page-label {
    position: absolute; width: 200px; margin-left: -100px; text-align: center;
    font-family: "Roboto", sans-serif; font-size: 14px; color: var(--label);
  }

  .panel { position: absolute; left: 16px; width: 1167px; overflow: hidden; border: 1px solid #555; }
  .panel--outside { top: 37px; height: 388px; }
  .panel--inside { top: 471px; height: 389px; }

  .block { position: absolute; }
  .photo { position: absolute; }

  /* Outside spread */
  .outside-left { left: 0; top: 0; width: 388px; height: 100%; background: var(--blue); }
  .placeholder-note {
    position: absolute; left: 78px; top: 170px; transform: rotate(-22deg); transform-origin: left top;
    color: var(--white); font-family: "Roboto", sans-serif; font-weight: 300; line-height: 1;
  }
  .placeholder-note .big { font-size: 25px; display: block; }
  .placeholder-note .small { font-size: 19px; display: block; margin-left: 20px; }

  .outside-back { left: 388px; top: 0; width: 390px; height: 100%; background: var(--navy); }
  .map { left: 513px; top: 37px; width: 141px; height: 164px; background: linear-gradient(160deg, #e6e3dc, #d4d8cf 60%, #c9d3c4); border: 1px solid #bbb; }
  .logo-card {
    position: absolute; background: var(--white); display: flex; align-items: center; justify-content: center; gap: 8px;
  }
  .logo-card .mark { width: 10px; height: 10px; border-radius: 50%; background: var(--blue); }
  .logo-card .name { font-family: "Roboto", sans-serif; font-weight: 400; color: var(--logo-ink); }
  .logo-card--back { left: 389px; top: 220px; width: 203px; height: 64px; }
  .logo-card--back .name { font-size: 13px; }

  .web-bar {
    position: absolute; height: 13px; background: var(--band);
    color: var(--white); font-family: "PT Sans", sans-serif; font-size: 9px; letter-spacing: 1.2px;
    display: flex; align-items: center; white-space: nowrap;
  }
  .web-bar--back { left: 593px; top: 284px; width: 300px; padding-left: 39px; }

  .contact { position: absolute; color: var(--text-light); font-size: 7.6px; line-height: 9.4px; letter-spacing: 0.2px; }
  .contact--firm { left: 419px; top: 309px; }
  .contact--firm .firm-name { font-weight: 700; font-size: 8px; margin-bottom: 5px; display: block; }
  .contact--phone { left: 560px; top: 334px; }

  .outside-front { left: 778px; top: 0; width: 389px; height: 100%; background: var(--navy); }
  .front-strip { left: 778px; top: 0; width: 112px; height: 299px; background: var(--blue); }
  .front-top { left: 890px; top: 0; width: 277px; height: 139px; background: var(--blue); }
  .front-title {
    position: absolute; left: 908px; top: 52px; color: var(--white);
    font-family: "Roboto", sans-serif; font-weight: 300; font-size: 19.5px; line-height: 24px;
  }
  .front-photo { left: 890px; top: 139px; width: 277px; height: 160px; background: linear-gradient(100deg, #5b6f8c, #b9c3d0 45%, #d9dde3 70%, #9aa9bd); }
  .front-veil { left: 890px; top: 139px; width: 94px; height: 249px; background: rgba(130, 150, 200, 0.45); }
  .family-photo { left: 778px; top: 309px; width: 112px; height: 79px; background: linear-gradient(90deg, #b58e6e, #e8d2bd 50%, #c8a27f); }
  .web-bar--front { left: 890px; top: 309px; width: 277px; padding-left: 119px; background: rgba(150, 165, 205, 0.75); }
  .logo-card--front { left: 987px; top: 323px; width: 180px; height: 65px; }
  .logo-card--front .name { font-size: 11.5px; }

  /* Inside spread */
  .inside-left { left: 0; top: 0; width: 388px; height: 100%; background: var(--blue); }
  .inside-center { left: 388px; top: 0; width: 390px; height: 100%; background: var(--navy); }
  .inside-right { left: 778px; top: 0; width: 389px; height: 100%; background: var(--navy); }

  .intro { position: absolute; left: 29px; top: 84px; width: 242px; color: var(--white); }
  .intro-title { font-family: "Roboto", sans-serif; font-weight: 300; font-size: 29px; line-height: 31px; }
  .intro-sub { font-family: "Roboto", sans-serif; font-weight: 300; font-size: 18px; line-height: 22px; margin-bottom: 10px; }
  .intro-copy { font-size: 9px; line-height: 14.2px; text-align: justify; }

  .column-strip { top: 0; height: 100%; background: var(--strip); }
  .column-strip--lorna { left: 416px; width: 65px; }
  .column-strip--miriam { left: 802px; width: 94px; }

  .band { position: absolute; }
  .band--lorna-top { left: 286px; top: 155px; width: 325px; height: 10px; background: linear-gradient(90deg, rgba(120,140,190,0.1), var(--band)); }
  .band--lorna-name { left: 286px; top: 168px; width: 437px; height: 13px; background: linear-gradient(90deg, var(--band), rgba(120,140,190,0.15)); }
  .band--miriam-top { left: 723px; top: 151px; width: 444px; height: 13px; background: linear-gradient(90deg, var(--band), rgba(120,140,190,0.7)); }
  .band--miriam-name { left: 894px; top: 169px; width: 273px; height: 8px; background: var(--band); }

  .portrait { top: 34px; width: 94px; height: 144px; }
  .portrait--lorna { left: 416px; background: linear-gradient(180deg, #7d8f6b, #c79a7a 40%, #8fb0d6 80%); }
  .portrait--miriam { left: 802px; background: linear-gradient(180deg, #9a9a88, #c89a80 35%, #b3282c 75%); }

  .advisor-name { position: absolute; color: var(--white); font-weight: 700; font-size: 10px; letter-spacing: 0.6px; line-height: 13px; }
  .advisor-name--lorna { left: 518px; top: 168px; }
  .advisor-name--miriam { left: 906px; top: 151px; }

  .advisor { position: absolute; top: 196px; color: var(--text-light); }
  .advisor--lorna { left: 416px; width: 345px; }
  .advisor--miriam { left: 802px; width: 345px; }
  .credentials { font-size: 7.6px; line-height: 8.8px; letter-spacing: 0.2px; margin-bottom: 12px; }
  .bio { font-size: 9.6px; line-height: 14.1px; letter-spacing: 0.15px; text-align: justify; }
</style>
</head>
<body>
  <div class="sheet-frame"></div>

  <span class="page-label" style="left:212px; top:18px;">Page 5</span>
  <span class="page-label" style="left:600px; top:18px;">Back Page 6</span>
  <span class="page-label" style="left:988px; top:18px;">Front Page 1</span>

  <section class="panel panel--outside">
    <div class="block outside-left">
      <p class="placeholder-note"><span class="big">what is here ?</span><span class="small">any text image provide me!</span></p>
    </div>

    <div class="block outside-back"></div>
    <div class="photo map" role="img" aria-label="Street map showing the office location in Mississauga"></div>
    <div class="logo-card logo-card--back"><span class="mark"></span><span class="name">Steadfast Money Partners</span></div>
    <div class="contact contact--firm">
      <span class="firm-name">Steadfast Money Partners</span>
      Northbay Securities Incorporated<br>
      Northbay Securities Insurance Inc.<br>
      382 Kettlewood Rd. East<br>
      Mississauga, ON L5R 7M4
    </div>
    <div class="contact contact--phone">
      Telephone: 905-555-0148<br>
      Toll Free: 1-866-555-0192<br>
      Fax: 905-555-0176
    </div>

    <div class="block outside-front"></div>
    <div class="block front-strip"></div>
    <div class="block front-top"></div>
    <h1 class="front-title">Choose your path.<br>Change your future.</h1>
    <div class="photo front-photo" role="img" aria-label="Advisor reviewing documents with a senior couple at a table"></div>
    <div class="photo family-photo" role="img" aria-label="Smiling multi-generation family group"></div>
    <div class="block front-veil"></div>
    <div class="web-bar web-bar--back">www.plantharvestsoon.ca</div>
    <div class="web-bar web-bar--front">www.plantharvestsoon.ca</div>
    <div class="logo-card logo-card--front"><span class="mark"></span><span class="name">Steadfast Money Partners</span></div>
  </section>

  <section class="panel panel--inside">
    <div class="block inside-left"></div>
    <div class="block inside-center"></div>
    <div class="block inside-right"></div>

    <div class="block column-strip column-strip--lorna"></div>
    <div class="block column-strip column-strip--miriam"></div>

    <div class="band band--lorna-top"></div>
    <div class="band band--lorna-name"></div>
    <div class="band band--miriam-top"></div>
    <div class="band band--miriam-name"></div>

    <div class="intro">
      <h2 class="intro-title">Building wealth</h2>
      <p class="intro-sub">to the next generation.</p>
      <p class="intro-copy">Financial security can be achieved through proper financial planning. Lorna and Miriam can provide you with a wealth management plan that covers investments, estate planning, retirement planning, tax planning, and pensions. Let the team from Steadfast Money Partners create a plan tailored to your specific situation.</p>
    </div>

    <div class="photo portrait portrait--lorna" role="img" aria-label="Portrait of advisor Lorna Feldskov"></div>
    <div class="photo portrait portrait--miriam" role="img" aria-label="Portrait of advisor Miriam Oakhurst"></div>

    <span class="advisor-name advisor-name--lorna">LORNA FELDSKOV</span>
    <span class="advisor-name advisor-name--miriam">MIRIAM OAKHURST</span>

    <article class="advisor advisor--lorna">
      <p class="credentials">Bsc, MBA, CPA, CA, CFP, FMA, CPCA<br>Senior Financial Advisor and Certified Financial Planner<br>Northbay Securities Incorporated and Northbay Securities Insurance Inc.</p>
      <p class="bio">Lorna is a tax-savvy financial advisor dedicated to helping her clients find the right blend of wealth creation and preservation for their long-term security and family needs. As a Chartered Accountant with executive-level business experience, Lorna also has an in-depth understanding of the unique financial planning requirements of time-challenged corporate executives and business owners.</p>
    </article>

    <article class="advisor advisor--miriam">
      <p class="credentials">BSEd, FMA, CFP, CPCA, FCSI, CIM<br>Senior Financial Advisor and Certified Financial Planner<br>Northbay Securities Incorporated and Northbay Securities Insurance Inc.</p>
      <p class="bio">Miriam’s drive and focus – honed as nationally ranked tennis player – are important assets her clients count on when it comes to helping them plan and execute game-changing financial strategies. She combines a sharp, analytical mind with a service-minded business approach that sets her apart from the crowd.</p>
    </article>
  </section>

  <span class="page-label" style="left:212px; top:863px;">left Page 2</span>
  <span class="page-label" style="left:600px; top:863px;">Center Page3</span>
  <span class="page-label" style="left:988px; top:863px;">Right Page 4</span>
</body>
</html>
```